Brightwire Hollow Business cards

one side I would like my logo (uploaded) and the other side I want my details. I'm an electrician in sydney. The logo side I'm happy with just a white background and our logo in the middle.

Details for other side
24/7 Sydney Electrician
Marcus Pell
0431 587 219
marcus@brightwirehollow.com.au
brightwirehollow.com.au
icons for facebook, instagram, linked in

Industry/Entity Type

electrician

Contact Information for Business Card

company info

```html
<!DOCTYPE html>
<html lang="en">
<head>
<meta charset="utf-8">
<title>Brightwire Hollow – Business Cards</title>
<link href="https://fonts.googleapis.com/css2?family=Lato:ital,wght@0,400;0,900;1,400;1,900&display=swap" rel="stylesheet">
<style>
  :root {
    --red: #e42313;
    --ink: #1d1d1b;
    --paper: #ffffff;
    --backdrop: #3b3c3f;
  }
  * { margin: 0; padding: 0; box-sizing: border-box; }
  html, body { width: 1200px; height: 1200px; overflow: hidden; }
  body {
    background: var(--backdrop);
    font-family: "Lato", Arial, sans-serif;
    position: relative;
  }
  .card {
    position: absolute;
    left: 161px;
    width: 878px;
    height: 513px;
    background: var(--paper);
    overflow: hidden;
  }
  .card--details { top: 61px; }
  .card--logo { top: 626px; }

  /* plain straight bands */
  .band { position: absolute; left: 0; right: 0; }
  .band--top-ink { top: 0; height: 34px; background: var(--ink); }
  .band--top-rule { top: 46px; left: 440px; height: 8px; background: var(--red); }
  .band--foot-ink { top: 418px; left: 440px; height: 50px; background: var(--ink); }
  .band--foot-red { top: 468px; height: 45px; background: var(--red); }

  .brand-name {
    position: absolute;
    color: var(--red);
    font-weight: 900;
    text-transform: uppercase;
    line-height: 0.95;
    letter-spacing: 0.02em;
  }
  .card--details .brand-name { left: 64px; top: 208px; font-size: 46px; }
  .card--logo .brand-name {
    left: 0; right: 0; top: 176px;
    text-align: center; font-size: 76px;
  }

  .holder-name {
    position: absolute;
    right: 62px;
    top: 142px;
    font-size: 36px;
    font-weight: 900;
    font-style: italic;
    color: var(--ink);
    text-transform: uppercase;
  }
  .contact-list { position: absolute; right: 62px; top: 236px; list-style: none; }
  .contact-list li {
    display: flex; align-items: center; justify-content: flex-end;
    height: 34px;
    font-size: 21px;
    color: var(--ink);
  }
  .contact-list svg { width: 17px; height: 17px; margin-left: 28px; flex: none; }

  .social-list { position: absolute; left: 60px; top: 368px; display: flex; gap: 16px; list-style: none; }
  .social-list li { width: 24px; height: 24px; border-radius: 50%; background: var(--ink); }

  .tagline {
    position: absolute;
    right: 62px;
    top: 429px;
    font-size: 23px;
    font-style: italic;
    color: var(--paper);
  }
</style>
</head>
<body>

<section class="card card--details" aria-label="Business card, details side">
  <div class="band band--top-ink"></div>
  <div class="band band--top-rule"></div>
  <div class="band band--foot-ink"></div>
  <div class="band band--foot-red"></div>

  <div class="brand-name">Brightwire<br>Hollow</div>

  <h1 class="holder-name">Marcus Pell</h1>

  <ul class="contact-list">
    <li>0431 587 219
      <svg viewBox="0 0 16 16"><rect x="4" y="1" width="8" height="14" rx="1.5" fill="none" stroke="var(--red)" stroke-width="1.6"/><circle cx="8" cy="12.5" r="0.9" fill="var(--red)"/></svg>
    </li>
    <li>marcus@brightwirehollow.com.au
      <svg viewBox="0 0 16 16"><rect x="1" y="3" width="14" height="10" rx="1" fill="var(--red)"/><polyline points="1.5,4 8,9 14.5,4" fill="none" stroke="var(--paper)" stroke-width="1.3"/></svg>
    </li>
    <li>brightwirehollow.com.au
      <svg viewBox="0 0 16 16"><circle cx="8" cy="8" r="6.5" fill="none" stroke="var(--red)" stroke-width="1.5"/><ellipse cx="8" cy="8" rx="2.8" ry="6.5" fill="none" stroke="var(--red)" stroke-width="1.2"/><line x1="1.5" y1="8" x2="14.5" y2="8" stroke="var(--red)" stroke-width="1.2"/></svg>
    </li>
  </ul>

  <ul class="social-list" aria-label="Social media">
    <li></li><li></li><li></li>
  </ul>

  <p class="tagline">24/7 Sydney Electrician</p>
</section>

<section class="card card--logo" aria-label="Business card, logo side">
  <div class="brand-name">Brightwire<br>Hollow</div>
</section>

</body>
</html>
```